"Velvet Petal Hour" Fashion Show Invitation design

We need an invitation design for our fashion show with the theme "Velvet Petal Hour"

the design will be the cover of the invitation, save the date cards, program etc

We are a philanthropic organization. Would like to incorporate florals, jewel tones or pastels etc... not sure if theres a way O or need) to incorporate fashion into that in an elegant way.

Text should read The Carrowfield Circle Presents "Velvet Petal Hour"
Updates

I'm looking for the design/image for the cover of our invitation- The only text needed is The Carrowfield Circle Presents Velvet Petal Hour I'm looking for feminine, elegant, florals etc...

Font styles to use
Serif
Decorative
Script

Colors
b768aa
e667a6
85cae6

Requirements
Must have
• jewel tones or pastels, flowers,
Nice to have
• fashion?

```html
<!DOCTYPE html>
<html lang="en">
<head>
<meta charset="utf-8">
<title>Velvet Petal Hour — Invitation Cover</title>
<link href="https://fonts.googleapis.com/css2?family=Antonio:wght@400;700&display=swap" rel="stylesheet">
<style>
  :root {
    --card-bg: #d8dde2;
    --card-shade: #cdd3d9;
    --ink: #ffffff;
    --petal-mauve: #b58a9c;
    --petal-rose: #c99aae;
    --petal-cream: #f3e4d6;
    --petal-heart: #d0456e;
    --sprig-blue: #8f9fcc;
    --stem-olive: #9a9a5e;
  }
  html, body {
    margin: 0;
    padding: 0;
    width: 1200px;
    height: 1200px;
    overflow: hidden;
  }
  .cover {
    position: relative;
    width: 1200px;
    height: 1200px;
    background: linear-gradient(160deg, var(--card-bg) 0%, var(--card-shade) 100%);
    font-family: "Antonio", "Arial Narrow", sans-serif;
    color: var(--ink);
    overflow: hidden;
  }
  .floral {
    position: absolute;
    border-radius: 50%;
  }
  .floral--mauve-large {
    left: 820px; top: 230px; width: 280px; height: 260px;
    background: radial-gradient(circle at 50% 50%, var(--petal-rose) 0%, var(--petal-mauve) 60%, rgba(181,138,156,0) 72%);
  }
  .floral--mauve-left {
    left: 150px; top: 560px; width: 270px; height: 270px;
    background: radial-gradient(circle at 50% 50%, var(--petal-rose) 0%, var(--petal-mauve) 60%, rgba(181,138,156,0) 72%);
  }
  .floral--cream-center {
    left: 620px; top: 680px; width: 190px; height: 170px;
    background: radial-gradient(circle at 50% 50%, var(--petal-heart) 0%, var(--petal-cream) 30%, var(--petal-cream) 58%, rgba(243,228,214,0) 70%);
  }
  .floral--cream-left {
    left: 30px; top: 800px; width: 150px; height: 150px;
    background: radial-gradient(circle at 50% 50%, var(--petal-heart) 0%, var(--petal-cream) 30%, var(--petal-cream) 58%, rgba(243,228,214,0) 70%);
  }
  .floral--sprig-blue {
    left: 90px; top: 430px; width: 150px; height: 170px;
    background: radial-gradient(ellipse at 50% 50%, rgba(143,159,204,0.55) 0%, rgba(143,159,204,0) 65%);
  }
  .floral--sprig-top {
    left: 770px; top: 30px; width: 220px; height: 200px;
    background: radial-gradient(ellipse at 50% 50%, rgba(143,159,204,0.45) 0%, rgba(143,159,204,0) 65%);
  }
  .floral--baby-breath {
    left: 120px; top: 140px; width: 380px; height: 140px;
    background: radial-gradient(ellipse at 50% 50%, rgba(154,154,94,0.35) 0%, rgba(154,154,94,0) 65%);
  }
  .floral--baby-breath-low {
    left: 360px; top: 960px; width: 520px; height: 160px;
    background: radial-gradient(ellipse at 50% 50%, rgba(154,154,94,0.3) 0%, rgba(154,154,94,0) 65%);
  }
  .presenter {
    position: absolute;
    left: 470px;
    top: 170px;
    margin: 0;
    font-weight: 400;
    font-size: 34px;
    letter-spacing: 0.5px;
    text-transform: uppercase;
    transform: skewX(-8deg);
  }
  .title {
    position: absolute;
    left: 0;
    top: 230px;
    margin: 0;
    font-weight: 700;
    text-transform: uppercase;
    line-height: 0.86;
  }
  .title__line {
    display: block;
    position: relative;
  }
  .title__line--one { left: 400px; font-size: 250px; }
  .title__line--two { left: 300px; font-size: 250px; }
  .title__line--three { left: 230px; font-size: 300px; }
</style>
</head>
<body>
  <main class="cover">
    <div class="floral floral--baby-breath" role="img" aria-label="Dried baby's breath stems laid across the card"></div>
    <div class="floral floral--sprig-top" role="img" aria-label="Small blue wildflower sprig"></div>
    <div class="floral floral--sprig-blue" role="img" aria-label="Small blue wildflower sprig"></div>
    <div class="floral floral--mauve-large" role="img" aria-label="Pressed mauve carnation bloom"></div>
    <div class="floral floral--mauve-left" role="img" aria-label="Pressed mauve carnation bloom"></div>
    <div class="floral floral--cream-center" role="img" aria-label="Cream petal with a deep pink centre"></div>
    <div class="floral floral--cream-left" role="img" aria-label="Cream petal with a deep pink centre"></div>
    <div class="floral floral--baby-breath-low" role="img" aria-label="Dried baby's breath stems"></div>

    <p class="presenter">The Carrowfield Circle Presents</p>
    <h1 class="title">
      <span class="title__line title__line--one">Velvet</span>
      <span class="title__line title__line--two">Petal</span>
      <span class="title__line title__line--three">Hour</span>
    </h1>
  </main>
</body>
</html>
```